HVAC Parts Distributor Website

We are working with an HVAC parts distributor to design a website. They primarily work with HVAC contractors.
They are similar to: https://www.brakenfieldparts.com, and https://www.ventorbin.com
Thank you for taking the time to consider designing a website for us. We are web developers based in Stockton, CA, USA. Most of our projects go through the same process. Understanding this process may help you win a project with us. We custom-code all of our websites in-house. We don’t have any requirements as to what tools you use for your design, but we ask that you follow these guidelines.
IMAGES:
If you use any images or icons in the design, we ask that you have a link to the asset so we can purchase the image/icon. Most of the designs we submit do not have the customer’s images on them unless they have some great images. Be creative; show us the feeling you are trying to portray with your image choices. Use any royalty-free site you choose. We subscribe to Veltrix and mainly use their images, but we can purchase images outside of Veltrix.
FONTS:
We ask that you identify the fonts you’re using in the design. This can be done in a message if you want. We typically use Quillon Fonts and Veltrix Fonts.
CONTENT:
We're always open to different content and ideas. We often submit designs with stock images so the client can see our vision. We typically take pictures after the website launch to use their images with our vision. Lorem Ipsum is fine for paragraphs, but we ask that you make the Headers with correct English. We want to be able to show the vision and identify the sections of the website.
INSPIRATION:
We typically add a couple of links in the brief of websites we like to help you get started in your design.
REVISIONS:
We do not often ask for revisions of the designs unless we see something in the design that may not appeal to the client. If there are slight changes that we want to make, we simply do that in the development process.
FEEDBACK:
We rarely give feedback on designs during the design process. We are working on many website projects and do not have the time to give feedback. We usually respond if your request is well thought out and asks specific questions, but a note asking “feedback, please” usually goes unanswered.
1 page

```html
<!DOCTYPE html>
<html lang="en">
<head>
<meta charset="utf-8">
<title>Northline HVAC Supply</title>
<link href="https://fonts.googleapis.com/css2?family=Poppins:wght@400;500;600;700;800&family=Inter:wght@400;500;600&display=swap" rel="stylesheet">
<style>
:root{
  --green:#94a817;
  --green-dark:#86991a;
  --olive-bg:#bdc38e;
  --ink:#222;
  --body:#444;
  --muted:#777;
  --line:#e4e4e4;
  --about-bg:#cfd1d9;
  --works-bg:#cdcf95;
  --footer:#000;
}
*{box-sizing:border-box;margin:0;padding:0}
html,body{width:1200px;height:3831px;overflow:hidden;background:#fff}
body{position:relative;font-family:"Inter",sans-serif;color:var(--body)}
h1,h2,h3,.heading{font-family:"Poppins",sans-serif}

/* header */
.site-header{position:absolute;top:0;left:0;width:1200px;height:96px;background:#fff}
.brand{position:absolute;left:112px;top:24px;display:flex;align-items:center;gap:10px;font-family:"Poppins",sans-serif;font-weight:800;font-size:30px;color:var(--ink);letter-spacing:.5px}
.brand-mark{width:22px;height:22px;background:var(--green)}
.search{position:absolute;left:550px;top:32px;width:308px;height:35px;border:1px solid #ddd;border-radius:3px;font-size:12px;color:#999;padding:9px 20px}
.search svg{position:absolute;right:12px;top:10px}
.account{position:absolute;left:915px;top:37px;display:flex;align-items:center;gap:12px;font-size:12px;font-weight:600;color:var(--ink)}
.dot-icon{width:24px;height:24px;border-radius:50%;background:#c8c8c8}
.cart{position:absolute;left:1058px;top:38px;width:24px;height:24px;border-radius:50%;background:#c7cf8d}
.main-nav{position:absolute;top:96px;left:0;width:1200px;height:60px;background:var(--green)}
.main-nav a{position:absolute;top:21px;color:#fff;font-family:"Poppins",sans-serif;font-size:15px;font-weight:500;text-decoration:none}

/* hero */
.hero{position:absolute;top:156px;left:0;width:1200px;height:600px;background:var(--olive-bg);overflow:hidden}
.hero-photo{position:absolute;left:0;top:0;width:1200px;height:600px}
.hero h1{position:absolute;left:674px;top:160px;font-size:52px;line-height:96px;font-weight:700;color:#fff;white-space:nowrap}
.hero p{position:absolute;left:677px;top:364px;width:460px;font-size:14px;line-height:26px;color:#fff}
.btn{display:inline-block;background:var(--green);color:#fff;font-family:"Poppins",sans-serif;font-weight:600;font-size:14px;text-align:center;border-radius:3px}
.hero .btn{position:absolute;left:677px;top:449px;width:144px;height:56px;line-height:56px}

/* categories */
.categories{position:absolute;top:843px;left:111px;display:flex;gap:18px}
.cat{width:148px;height:128px;background:#fff;box-shadow:0 2px 10px rgba(0,0,0,.12);border-radius:3px;text-align:center;padding-top:24px;font-family:"Poppins",sans-serif;font-weight:500;font-size:16px;color:#333}
.cat svg{display:block;margin:0 auto 12px}
.cat.active{background:var(--green);color:#fff}

/* about */
.about{position:absolute;top:1073px;left:0;width:1200px;height:643px;background:linear-gradient(180deg,#c5c7d4,#d3d4da)}
.about-outline{position:absolute;left:111px;top:140px;width:247px;height:410px;border:3px solid var(--green)}
.about-photo{position:absolute;left:146px;top:93px;width:464px;height:416px;background:linear-gradient(135deg,#8c6a45 0%,#e7e4e0 40%,#3b5a8c 75%,#c9c9c9 100%)}
.about-frame{position:absolute;left:161px;top:107px;width:435px;height:390px;border:2px solid #fff}
.about h2{position:absolute;left:667px;top:100px;width:420px;font-size:29px;line-height:43px;font-weight:600;color:var(--green)}
.about p{position:absolute;left:667px;top:214px;width:425px;font-size:15px;line-height:26px;color:#333}
.about .btn{position:absolute;left:667px;top:462px;width:144px;height:55px;line-height:55px}

/* testimonials */
.section-title{position:absolute;left:0;width:1200px;text-align:center;font-size:30px;font-weight:600;color:var(--green)}
.tcard{position:absolute;top:1888px;height:292px;background:#fff;box-shadow:0 2px 12px rgba(0,0,0,.13)}
.tphoto{position:absolute;top:9px;height:274px}
.tcard p{position:absolute;font-size:14.5px;line-height:26px;color:#444;text-align:justify}
.stars{position:absolute;color:var(--green);font-size:13px;letter-spacing:1px}
.tname{position:absolute;font-size:16px;color:var(--green);font-weight:500}
.trole{position:absolute;font-size:11px;color:#888}
.quote{position:absolute;width:28px;height:28px;border-radius:50%;background:var(--green)}
.arrow{position:absolute;top:2227px;width:37px;height:37px;border-radius:50%;border:2px solid var(--green)}
.arrow.filled{background:var(--green)}
.arrow svg{position:absolute;left:10px;top:10px}

/* how it works */
.works{position:absolute;top:2350px;left:0;width:1200px;height:600px;background:linear-gradient(180deg,#cfd095,#d8d9a8)}
.works h2{position:absolute;top:83px;left:0;width:1200px;text-align:center;font-size:30px;font-weight:600;color:#fff}
.wcard{position:absolute;top:171px;width:298px;height:334px;background:#fff;border-radius:4px;text-align:center}
.wcard svg{margin-top:40px}
.wcard h3{margin-top:30px;font-size:20px;font-weight:600;color:#222}
.wcard p{margin:16px auto 0;width:250px;font-size:14.5px;line-height:26px;color:#444}
.wcard a{display:block;margin-top:16px;font-family:"Poppins",sans-serif;font-weight:500;font-size:14px;color:var(--green);text-decoration:none}

/* brands */
.brand-circle{position:absolute;top:3127px;width:156px;height:156px;border-radius:50%;border:11px solid #e6e8cf;background:#fff;display:flex;align-items:center;justify-content:center;font-family:"Poppins",sans-serif;font-weight:600;font-size:18px;color:#333}
.brand-circle.active{border-color:var(--green)}
.dots{position:absolute;top:3326px;left:569px;display:flex;gap:7px}
.dots span{width:10px;height:10px;border-radius:50%;background:#ccc}
.dots span.on{background:var(--green)}
.chat{position:absolute;left:1048px;top:3383px;width:40px;height:40px;border-radius:50%;background:#c4cb90}

/* footer */
.site-footer{position:absolute;top:3426px;left:0;width:1200px;height:405px;background:var(--footer);color:#fff}
.f-brand{position:absolute;left:112px;top:118px;display:flex;align-items:center;gap:10px;font-family:"Poppins",sans-serif;font-weight:800;font-size:30px;color:#fff}
.f-brand .brand-mark{width:22px;height:22px}
.social{position:absolute;top:235px;left:112px;display:flex;gap:15px}
.social span{width:40px;height:40px;border-radius:50%;background:#fff}
.f-col h4{font-family:"Poppins",sans-serif;font-size:17px;font-weight:600;margin-bottom:20px}
.f-col{position:absolute;top:111px;font-size:14.5px}
.f-col ul{list-style:none;line-height:26px}
.contact-row{display:flex;gap:14px;line-height:23px;margin-bottom:11px}
.contact-row svg{flex:none;margin-top:3px}
.newsletter{position:absolute;left:863px;top:149px;width:225px;height:38px;background:#fff;border-radius:3px;color:#888;font-size:14px;padding:10px 14px}
.newsletter span{position:absolute;right:0;top:0;width:54px;height:38px;background:var(--green);border-radius:0 3px 3px 0}
.copy{position:absolute;left:0;top:358px;width:1200px;text-align:center;font-size:14px}
</style>
</head>
<body>

<header class="site-header">
  <div class="brand"><span class="brand-mark"></span>Northline HVAC Supply</div>
  <div class="search">Search
    <svg width="14" height="14" viewBox="0 0 14 14"><circle cx="6" cy="6" r="4.5" fill="none" stroke="#aaa" stroke-width="1.5"/><path d="M9.5 9.5 13 13" stroke="#aaa" stroke-width="1.5"/></svg>
  </div>
  <div class="account"><span class="dot-icon"></span>ACCOUNT</div>
  <div class="cart"></div>
</header>

<nav class="main-nav">
  <a style="left:149px">HOME</a>
  <a style="left:248px">HAVC EQUIPMENT</a>
  <a style="left:435px">HAVCR PARTS</a>
  <a style="left:591px">MOTORS</a>
  <a style="left:708px">SUPPLIES</a>
  <a style="left:836px">ELECTRICAL</a>
  <a style="left:980px">CONTACT</a>
</nav>

<section class="hero">
  <svg class="hero-photo" viewBox="0 0 1200 600" role="img" aria-label="Technician servicing an outdoor air conditioning unit">
    <defs><linearGradient id="heroPhoto" x1="0" y1="0" x2="1" y2="1"><stop offset="0" stop-color="#c9d3da"/><stop offset=".5" stop-color="#dde2e6"/><stop offset="1" stop-color="#7f8a93"/></linearGradient></defs>
    <polygon points="0,0 590,0 440,600 0,600" fill="url(#heroPhoto)"/>
    <polygon points="640,0 697,0 547,600 490,600" fill="#94a817"/>
  </svg>
  <h1>NORTHLINE HVAC<br>SUPPLY</h1>
  <p>Lorem ipsum dolor sit amet, consectetur adipiscing elit, sed do eiusmod tempor incididunt ut labore et dolore magna aliqua.</p>
  <a class="btn">GET STARTED</a>
</section>

<div class="categories">
  <div class="cat"><svg width="60" height="44" viewBox="0 0 60 44" fill="none" stroke="#94a817" stroke-width="2"><rect x="4" y="14" width="30" height="14"/><path d="M34 18h14v20M20 14V6M12 6h16"/></svg>PLUMBING</div>
  <div class="cat"><svg width="60" height="44" viewBox="0 0 60 44" fill="none" stroke="#94a817" stroke-width="2"><rect x="8" y="18" width="44" height="22" rx="3"/><path d="M16 18v22M24 18v22M32 18v22M40 18v22M22 4v8M30 4v8M38 4v8"/></svg>HEATING</div>
  <div class="cat active"><svg width="60" height="44" viewBox="0 0 60 44" fill="none" stroke="#fff" stroke-width="2"><rect x="4" y="6" width="52" height="20" rx="3"/><path d="M10 20h40M16 32l-3 8M26 32v8M34 32v8M44 32l3 8"/></svg>HVAC</div>
  <div class="cat"><svg width="60" height="44" viewBox="0 0 60 44" fill="none" stroke="#94a817" stroke-width="2"><circle cx="20" cy="10" r="5"/><circle cx="40" cy="10" r="5"/><path d="M12 24c0-5 16-5 16 0M32 24c0-5 16-5 16 0M6 36h48"/></svg>VALVES</div>
  <div class="cat"><svg width="60" height="44" viewBox="0 0 60 44" fill="none" stroke="#94a817" stroke-width="2"><path d="M12 4l36 36M48 4L12 40"/></svg>TOOLS</div>
  <div class="cat"><svg width="60" height="44" viewBox="0 0 60 44" fill="none" stroke="#94a817" stroke-width="2"><circle cx="30" cy="22" r="18"/><path d="M26 12v8M34 12v8M24 20h12v6l-6 4-6-4z"/></svg>ELECTRICAL</div>
</div>

<section class="about">
  <div class="about-outline"></div>
  <div class="about-photo" role="img" aria-label="Hand replacing a ceiling air filter"></div>
  <div class="about-frame"></div>
  <h2>ABOUT NORTHLINE HVAC SUPPLY</h2>
  <p>Lorem ipsum dolor sit amet, consectetur adipiscing elit, sed do eiusmod tempor incididunt ut labore et dolore magna aliqua. Ut enim ad minim veniam, quis nostrud exercitation ullamco laboris nisi ut aliquip ex ea commodo consequat. Duis aute irure dolor in reprehenderit in voluptate velit esse cillum dolore eu fugiat nulla pariatur. Excepteur sint occaecat cupidatat non proident, sunt in culpa qui officia deserunt mollit anim id est laborum.</p>
  <a class="btn">LEARN MORE</a>
</section>

<h2 class="section-title" style="top:1794px">CUSTOMERS SAY..</h2>

<div class="tcard" style="left:-40px;width:233px;overflow:hidden">
  <p style="left:38px;top:45px;width:160px">sectetur adipiscing elit, unt ut labore et dolore n veniam, quis nostrud nisi ut aliquip ex ea</p>
  <div class="stars" style="left:118px;top:204px">★★★★★</div>
</div>

<div class="tcard" style="left:233px;width:733px">
  <div class="tphoto" role="img" aria-label="Portrait of a smiling customer" style="left:10px;width:256px;background:linear-gradient(180deg,#9a9a9a,#b9a583)"></div>
  <p style="left:323px;top:45px;width:372px">Lorem ipsum dolor sit amet, consectetur adipiscing elit, sed do eiusmod tempor incididunt ut labore et dolore magna aliqua. Ut enim ad minim veniam, quis nostrud exercitation ullamco laboris nisi ut aliquip ex ea commodo consequat.</p>
  <div class="tname" style="left:323px;top:207px">Dan Mercer</div>
  <div class="quote" style="left:429px;top:203px"></div>
  <div class="trole" style="left:323px;top:236px">Lorem ipsum dolor</div>
  <div class="stars" style="left:620px;top:210px">★★★★★</div>
</div>

<div class="tcard" style="left:1007px;width:233px">
  <div class="tphoto" role="img" aria-label="Portrait of a customer holding a folder" style="left:9px;width:220px;background:linear-gradient(180deg,#e9e9e9,#6b7d8a)"></div>
</div>

<div class="arrow" style="left:555px"><svg width="14" height="14" viewBox="0 0 14 14"><path d="M9 2 4 7l5 5" fill="none" stroke="#94a817" stroke-width="2"/></svg></div>
<div class="arrow filled" style="left:608px"><svg width="14" height="14" viewBox="0 0 14 14"><path d="M5 2l5 5-5 5" fill="none" stroke="#fff" stroke-width="2"/></svg></div>

<section class="works">
  <h2>HOW IT WORKS</h2>
  <div class="wcard" style="left:111px">
    <svg width="96" height="64" viewBox="0 0 96 64" fill="none" stroke="#94a817" stroke-width="2.5"><rect x="4" y="6" width="56" height="40"/><path d="M60 20h18l12 14v12H60M22 26l8 8 14-16"/><circle cx="20" cy="52" r="6"/><circle cx="74" cy="52" r="6"/></svg>
    <h3>Free shipping</h3>
    <p>Lorem ipsum dolor sit amet, consectetur adipiscing elit, sed do eiusmod tempor et aliqua.</p>
    <a>LEARN MORE</a>
  </div>
  <div class="wcard" style="left:451px">
    <svg width="96" height="84" viewBox="0 0 96 84" fill="none" stroke="#94a817" stroke-width="2.5" style="margin-top:30px"><path d="M30 30l16-14 16 14v44H30z"/><circle cx="46" cy="50" r="9"/><path d="M46 16V4"/></svg>
    <h3 style="margin-top:20px">Lower Prices</h3>
    <p>Lorem ipsum dolor sit amet, consectetur adipiscing elit, sed do eiusmod tempor et aliqua.</p>
    <a>LEARN MORE</a>
  </div>
  <div class="wcard" style="left:790px">
    <svg width="80" height="76" viewBox="0 0 80 76" fill="none" stroke="#94a817" stroke-width="2.5" style="margin-top:38px"><circle cx="40" cy="38" r="34"/><path d="M24 28l16-8 16 8v20l-16 8-16-8zM24 28l16 8 16-8M40 36v20"/></svg>
    <h3 style="margin-top:22px">Free Returns</h3>
    <p>Lorem ipsum dolor sit amet, consectetur adipiscing elit, sed do eiusmod tempor et aliqua.</p>
    <a>LEARN MORE</a>
  </div>
</section>

<h2 class="section-title" style="top:3030px">TRUSTED BRANDS</h2>
<div class="brand-circle" style="left:113px">Coldray</div>
<div class="brand-circle active" style="left:319px">Airvane</div>
<div class="brand-circle" style="left:524px">Brisko</div>
<div class="brand-circle" style="left:729px">Frostel</div>
<div class="brand-circle" style="left:933px">Thermiq</div>
<div class="dots"><span></span><span class="on"></span><span></span><span></span></div>
<div class="chat"></div>

<footer class="site-footer">
  <div class="f-brand"><span class="brand-mark" style="background:#94a817"></span>Northline HVAC</div>
  <div class="social"><span aria-label="Social profile"></span><span aria-label="Social profile"></span><span aria-label="Social profile"></span><span aria-label="Social profile"></span></div>

  <div class="f-col" style="left:421px">
    <h4>QUICK LINKS</h4>
    <ul><li>Home</li><li>HAVC Equipment</li><li>HAVCR Parts</li><li>Motors</li><li>Supplies</li><li>Electrical</li><li>Contact</li></ul>
  </div>

  <div class="f-col" style="left:583px">
    <h4>CONTACT US</h4>
    <div class="contact-row"><svg width="14" height="18" viewBox="0 0 14 18"><path d="M7 0a7 7 0 0 0-7 7c0 5 7 11 7 11s7-6 7-11a7 7 0 0 0-7-7z" fill="#fff"/><circle cx="7" cy="7" r="2.5" fill="#000"/></svg><span>Lorem ipsum dolor sit<br>amet, consectetur</span></div>
    <div class="contact-row"><svg width="16" height="16" viewBox="0 0 16 16"><path d="M3 1l3 3-2 2c1 2 3 4 6 6l2-2 3 3-2 2C7 15 1 9 1 3z" fill="#fff"/></svg><span>+1 (555) 014 2290</span></div>
    <div class="contact-row"><svg width="16" height="14" viewBox="0 0 16 14"><rect x="0" y="1" width="16" height="12" fill="#fff"/><path d="M0 1l8 6 8-6" fill="none" stroke="#000" stroke-width="1.5"/></svg><span>info@northlinehvacsupply.com</span></div>
  </div>

  <div class="f-col" style="left:863px"><h4>NEWSLETTER</h4></div>
  <div class="newsletter">Ener email<span></span></div>

  <div class="copy">©Copyrights 2023 Northline HVAC Supply &nbsp;|&nbsp; All Rights Reserved</div>
</footer>

</body>
</html>
```